Product Launch HTML Email Design

Lumen Crate. Email blast for quickest and easiest property research tool. quickest and easiest way to find property ownership records including names, phone numbers, and mailing addresses. brokers spend less time collecting information and more time prospecting.
Updates
Also, it has to be run by a spam checker. Thank you I have posted under the new file, a skyline picture that HAS to be use. The old skyline can''t be used. I apologize for any inconvenience this may have caused. Please remember that it has to be HTML design. If it''s not, the flyer won''t be visible to recepients that don''t have allow images on their emails.
Target Market(s)
Males, ages 20-55, income 100k/yr+, commercial real estate brokers
Industry/Entity Type
Product
Requirements
Must have
- Logo. Design must be consistent with http://www.lumencrate-example.com/blogger which will be used as the landing page for the email blast as well. Email is encouraged to link to this page. $50/month for unlimited property records.
Nice to have
- suggested subject lines
Should not have
- Should not look cluttered. Message should not be in a big image only in case the viewer does not select to view images. Should not look cluttered.

```html
<!DOCTYPE html>
<html lang="en">
<head>
<meta charset="utf-8">
<title>Lumen Crate – Property Research Tool</title>
<link href="https://fonts.googleapis.com/css2?family=Ubuntu:wght@400;500&display=swap" rel="stylesheet">
<style>
  :root {
    --brand-green: #3f9600;
    --brand-green-light: #8ccd2a;
    --text-grey: #7d7d7d;
    --body-grey: #6e6e6e;
    --paper: #ffffff;
    --texture: #e6e6e6;
    --sky-top: #8c8c8c;
    --sky-mid: #b9b9b9;
    --water: #5d5d5d;
  }
  * { margin: 0; padding: 0; box-sizing: border-box; }
  html, body { width: 674px; height: 1200px; overflow: hidden; background: var(--paper); }
  body { font-family: "Ubuntu", sans-serif; }
  .email { position: relative; width: 674px; height: 1200px; overflow: hidden; background: var(--paper); }

  .header { position: absolute; left: 0; top: 0; width: 674px; height: 234px; background: var(--paper); }
  .brand-mark { position: absolute; left: 40px; top: 42px; width: 150px; height: 150px; border-radius: 50%;
    background: var(--brand-green-light); }
  .brand-name { position: absolute; left: 288px; top: 46px; font-size: 45px; font-weight: 500;
    color: var(--brand-green); line-height: 1; }
  .tagline { position: absolute; left: 289px; top: 118px; font-size: 29px; font-weight: 400;
    color: var(--text-grey); line-height: 1; }

  .skyline { position: absolute; left: 0; top: 234px; width: 674px; height: 452px;
    background: linear-gradient(to bottom, var(--sky-top) 0%, var(--sky-mid) 55%, #d4d4d4 72%, var(--water) 80%, #6a6a6a 100%); }

  .content { position: absolute; left: 0; top: 686px; width: 674px; height: 514px; background: var(--texture); }

  .headline-band { position: absolute; left: 0; top: 25px; width: 674px; height: 87px;
    background: var(--brand-green); color: var(--paper); font-size: 33px; font-weight: 500;
    line-height: 41px; padding: 4px 22px 0; }

  .copy-line { position: absolute; left: 0; width: 674px; height: 44px; padding-left: 22px;
    font-size: 31px; font-weight: 500; line-height: 44px; white-space: nowrap; }
  .copy-line.plain { color: var(--body-grey); }
  .copy-line.banded { background: var(--brand-green); color: var(--paper); }
</style>
</head>
<body>
<div class="email">
  <header class="header">
    <div class="brand-mark"></div>
    <div class="brand-name">Lumen Crate</div>
    <div class="tagline">Let Brokers be Brokers</div>
  </header>

  <div class="skyline" role="img" aria-label="Black and white photo of a waterfront city skyline with high-rise towers across the bay"></div>

  <section class="content">
    <h1 class="headline-band">Quickest and easiest property research tool</h1>
    <p class="copy-line plain" style="top:148px">Quickest and easiest way to find</p>
    <p class="copy-line banded" style="top:200px">property ownership records including</p>
    <p class="copy-line plain" style="top:252px">names, phone numbers,and mailing</p>
    <p class="copy-line banded" style="top:302px">addresses. brokers spend less time</p>
    <p class="copy-line plain" style="top:355px">collecting information and more time</p>
    <p class="copy-line banded" style="top:406px">prospecting.</p>
  </section>
</div>
</body>
</html>
```